Hello,
We’re looking for a new WordPress website for Follow The Tide, our company offering unique well-being retreats and workshops.
We currently have a website online (you can consult it : www.followthetide.ch), but we now need to build a new site on WordPress — more flexible, more intuitive to manage, and better aligned with our evolving needs.

What we’re looking for:
A new userfriendly WordPress site, with:
Inspiring, elegant, and modern design
Smooth user experience on desktop and mobile
Innovative design proposals – we want to be inspired !
SEO best practices
Respect of our existing color palette
The final website will need to be set up on our existing hosting provider (details can be shared later)

Pages to Include:
- Home
- Our Story
- Our Stays - with links to 5 individual pages, each describing one of our stays in detail.
- Activities – with potential links to individual descriptive pages
- Agenda
- Our Charter
- The Team
- Contact
- Blog

Required Features:
- Space for photos and videos
- Sections for testimonials and press articles
- Blog/article layout with strong readability
- Easy-to-update backend for future content
- Newsletter sign-up (pop-up and in footer)
- Additional pop-up on/off
- “Request info” buttons
- “Booking request” buttons
- Integration of our 4 pillars - Breathe · Feel · Connect · Experience - in the design (They’re currently in the footer, but we’re open to creative suggestions)

Who we are :
Follow The Tide offers well-being and personal growth stays but with a very different spirit.
We’re not a classic wellness brand. Our approach is professional, joyful, and grounded.
We create spaces where people can take a real break — breathe, slow down, and reconnect with themselves.
During our stays, people are welcomed like friends:
with warmth, respect, and no pressure.
Each program combines practices like breathwork, movement, creativity, coaching, and massages in a relaxed, beautiful setting of the French Alps.
What makes us different:
A friendly and down-to-earth atmosphere
A wide mix of activities.
A mix of inner work and simple pleasures
Private rooms, nourishing food, and shared moments
Time to talk, to laugh, to walk, or just be silent together - and feel free to be yourself
Our guests come to pause.
They leave feeling lighter, aligned, and full of life

```html
<!DOCTYPE html>
<html lang="en">
<head>
<meta charset="utf-8">
<title>Follow The Tide – Well-being Retreats</title>
<link href="https://fonts.googleapis.com/css2?family=Arimo:wght@400;700&display=swap" rel="stylesheet">
<style>
:root{
  --teal:#62c1c0;
  --teal-dark:#4eaead;
  --ink:#120909;
  --text:#3a3a3a;
  --paper:#fbf9f7;
  --white:#ffffff;
}
*{margin:0;padding:0;box-sizing:border-box}
html,body{width:1200px;height:5025px;overflow:hidden}
body{font-family:"Arimo",Arial,sans-serif;background:var(--paper);color:var(--text);position:relative}
.abs{position:absolute}
section,header,footer{position:absolute;left:0;width:1200px;overflow:hidden}

/* Hero */
.hero{top:0;height:853px}
.hero-photo{position:absolute;inset:0;background:linear-gradient(180deg,#9aa7b0 0%,#8b98a3 35%,#5d6a74 62%,#2f3940 82%,#1d2328 100%)}
.brand{left:0;width:1200px;top:38px;text-align:center;color:var(--white);font-weight:700;font-size:40px;letter-spacing:4px}
.nav{top:134px;left:0;width:1200px;height:66px}
.nav a{position:absolute;top:0;height:66px;line-height:66px;color:var(--white);font-weight:700;font-size:26px;text-decoration:none}
.nav a.active{background:var(--teal);padding:0 14px}
.social{top:146px;width:44px;height:44px;border-radius:50%;background:#e8e8e8}
.hero-kicker{top:355px;width:1200px;left:12px;text-align:center;color:var(--white);font-size:34px}
.hero-title{top:400px;width:1200px;left:12px;text-align:center;color:var(--white);font-weight:700;font-size:49px;line-height:50px}
.hero-sub{top:508px;width:1200px;left:12px;text-align:center;color:var(--white);font-weight:700;font-size:17px;line-height:27px}
.btn-booking{top:608px;left:478px;width:272px;height:68px;background:var(--teal);color:var(--white);font-weight:700;font-size:24px;line-height:68px;text-align:center}

/* Pillars */
.pillars{top:853px;height:686px;background:var(--teal)}
.pillar{width:365px;color:var(--white)}
.pillar-icon{width:74px;height:74px;border:3px solid var(--white);border-radius:50%}
.pillar h3{font-size:32px;font-weight:700;line-height:34px}
.pillar p{font-size:12.5px;line-height:20.5px}
.pillar-photo-wrap{left:388px;top:125px;width:420px;height:450px;background:var(--white);border-radius:52% 48% 46% 54%/50% 44% 56% 50%}
.pillar-photo{left:410px;top:140px;width:380px;height:415px;border-radius:50%;background:radial-gradient(circle at 50% 40%,#f4efea 0%,#e4ddd5 55%,#cfc6bc 100%)}

/* Story */
.story{top:1539px;height:445px;background:var(--ink);text-align:center}
.teal-title{color:var(--teal);font-weight:700;font-size:40px}
.divider{height:2px;width:130px;background:var(--white)}
.story p{position:absolute;top:222px;left:190px;width:860px;color:var(--white);font-size:18px;line-height:30px}

/* Services band */
.services{top:1984px;height:186px;background:var(--teal)}
.services h2{left:62px;top:58px;color:var(--white);font-size:38px;line-height:40px;font-weight:700}
.service-icon{top:30px;width:125px;height:125px;border:3px solid rgba(255,255,255,.8);border-radius:18px}
.vline{top:32px;width:3px;height:126px;background:var(--white)}

/* Stays */
.stays{top:2170px;height:522px;background:var(--paper)}
.section-title{font-size:36px;font-weight:700;color:var(--text)}
.stays p{left:62px;top:205px;width:595px;font-size:18px;line-height:29.5px}
.video{left:692px;top:36px;width:436px;height:451px;background:linear-gradient(160deg,#b9ad97 0%,#a58c5e 45%,#8b6d3c 75%,#6e5630 100%)}

/* Gallery */
.gallery{top:2692px;height:414px;background:var(--paper)}
.gallery-photo{top:118px;height:262px}

/* Testimonials */
.testimonials{top:3106px;height:576px;background:var(--teal);color:var(--white);text-align:center}
.avatar{width:100px;height:100px;border-radius:50%;background:linear-gradient(160deg,#d7b59c,#8c5d45)}
.testimonial{width:460px}
.testimonial h4{font-size:28px;font-weight:700;margin-bottom:8px}
.testimonial p{font-size:14.5px;line-height:23.5px}
.stars{display:flex;justify-content:center;gap:8px;margin-top:30px}

/* Blogs */
.blogs{top:3682px;height:538px;background:var(--paper)}
.blog{width:305px}
.blog-photo{height:200px}
.blog p{font-size:10px;line-height:16px;margin-top:14px;color:#444}
.read-more{display:inline-block;margin-top:6px;background:var(--teal);color:var(--white);font-size:17px;padding:3px 8px}

/* Contact / newsletter */
.contact{top:4220px;height:618px}
.contact-photo{position:absolute;inset:0;background:linear-gradient(110deg,#b4ad8c 0%,#d9d1bd 35%,#e6dfd3 60%,#c9a78d 80%,#a88666 100%)}
.thanks-photo{left:280px;top:62px;width:300px;height:368px;background:linear-gradient(170deg,#c9c7c1 0%,#6b3a2a 55%,#9b1b2b 100%)}
.thanks-panel{left:580px;top:62px;width:365px;height:368px;background:var(--teal);color:var(--white);text-align:center}
.thanks-panel h2{margin-top:88px;font-size:38px;font-weight:700}
.thanks-panel p{margin:14px auto 0;width:290px;font-size:16px;line-height:25px}
.btn-download{position:absolute;left:54px;top:228px;width:258px;height:62px;background:#2a2a2a;color:var(--white);font-size:17px;line-height:22px;padding-top:9px}
.newsletter-title{top:464px;width:1200px;left:22px;text-align:center;color:var(--white);font-size:28px;font-weight:700}
.email{left:287px;top:510px;width:413px;height:52px;background:var(--white);color:#777;font-size:14px;line-height:52px;padding-left:34px}
.btn-signup{left:700px;top:510px;width:232px;height:52px;background:var(--teal);color:var(--white);font-size:28px;font-weight:700;line-height:52px;text-align:center}

/* Footer */
.footer{top:4838px;height:187px;background:var(--ink);color:var(--white)}
.footer-brand{left:35px;top:48px;font-size:30px;font-weight:700;letter-spacing:2px}
.footer-nav a{position:absolute;color:var(--white);font-size:19px;text-decoration:none}
.footer-icon{top:60px;width:46px;height:46px}
.copyright{top:138px;width:1200px;left:0;text-align:center;font-size:22px}
</style>
</head>
<body>

<header class="hero">
  <div class="hero-photo" role="img" aria-label="Misty alpine mountain range at dusk"></div>
  <div class="abs brand">FOLLOW THE TIDE</div>
  <nav class="abs nav">
    <a style="left:64px">HOME</a>
    <a class="active" style="left:166px">OUR STORY</a>
    <a style="left:370px">SERVICES</a>
    <a style="left:542px">THE TEAM</a>
    <a style="left:720px">BLOGS</a>
    <a style="left:873px">CONTACT</a>
  </nav>
  <span class="abs social" style="left:1034px" aria-label="Social link"></span>
  <span class="abs social" style="left:1091px" aria-label="Social link"></span>
  <div class="abs hero-kicker">FOLLOW THE TIDE</div>
  <h1 class="abs hero-title">INVITES YOU ON AN INNER<br>AND OUTER JOURNEY</h1>
  <p class="abs hero-sub">a unique experience where each step reconnects you with<br>your vitality and well-being</p>
  <div class="abs btn-booking">BOOKING NOW</div>
</header>

<section class="pillars">
  <div class="abs pillar-photo-wrap"></div>
  <div class="abs pillar-photo" role="img" aria-label="Woman meditating cross-legged in lotus pose"></div>

  <div class="abs pillar" style="left:40px;top:100px">
    <div class="pillar-icon" style="margin-left:140px" role="img" aria-label="Breath icon"></div>
    <h3 style="margin-left:92px;margin-top:8px">BREATH</h3>
    <p>Slow down with guided breathwork sessions that calm the mind, open the chest and bring you back to the present moment, one easy breath at a time, surrounded by the quiet peaks of the Alps.</p>
  </div>
  <div class="abs pillar" style="left:38px;top:360px">
    <div class="pillar-icon" style="margin-left:130px" role="img" aria-label="Feel icon"></div>
    <h3 style="margin-left:128px;margin-top:0">FEEL</h3>
    <p>Give space to every emotion through movement, creativity and gentle coaching, in a setting where nothing is expected and you are free to simply notice what is alive in you today and let it be.</p>
  </div>
  <div class="abs pillar" style="left:812px;top:110px">
    <div class="pillar-icon" style="margin-left:140px" role="img" aria-label="Connect icon"></div>
    <h3 style="margin-left:86px;margin-top:6px">CONNECT</h3>
    <p>Share meals, long walks and honest conversations with a small group of guests who arrive as strangers and leave as friends, welcomed with warmth, respect and plenty of laughter along the way, every single day.</p>
  </div>
  <div class="abs pillar" style="left:812px;top:380px">
    <div class="pillar-icon" style="margin-left:150px" role="img" aria-label="Experience icon"></div>
    <h3 style="margin-left:68px;margin-top:0">EXPERIENCE</h3>
    <p>Discover a wide mix of practices, from massages to mountain hikes, with private rooms, nourishing food and all the time you need to rest, play and feel fully yourself again before heading home.</p>
  </div>
</section>

<section class="story">
  <h2 class="abs teal-title" style="left:0;width:1260px;top:76px">OUR STORY</h2>
  <div class="abs divider" style="left:566px;top:168px"></div>
  <p>Lorem ipsum dolor sit amet, consectetur adipiscing elit, sed do eiusmod tempor incididunt ut labore et dolore magna aliqua. Ut enim ad minim veniam, quis nostrud exercitation ullamco laboris nisi ut aliquip ex ea commodo consequat Duis aute irure dolor in reprehenderit in voluptate velit esse cillum dolore eu fugiat nulla pariatur. Excepteur, sint occaecat cupidatat non proident, sunt in culpa qui officia deserunt mollit anim id es laborum.</p>
</section>

<section class="services">
  <h2 class="abs">OUR<br>SERVICES</h2>
  <div class="abs service-icon" style="left:405px" role="img" aria-label="Facial treatment icon"></div>
  <div class="abs vline" style="left:582px"></div>
  <div class="abs service-icon" style="left:620px" role="img" aria-label="Meditation icon"></div>
  <div class="abs vline" style="left:792px"></div>
  <div class="abs service-icon" style="left:830px" role="img" aria-label="Leaf icon"></div>
  <div class="abs vline" style="left:981px"></div>
  <div class="abs service-icon" style="left:1012px" role="img" aria-label="Spa stones and candle icon"></div>
</section>

<section class="stays">
  <h2 class="abs section-title" style="left:62px;top:88px">OUR STAYS</h2>
  <p class="abs">Lorem ipsum dolor sit amet, consectetur adipiscing elit, sed do eiusmod tempor incididunt ut labore et dolore magna aliqua. Ut enim ad minim veniam, quis nostrud exercitation ullamco laboris nisi ut aliquip ex ea commodo consequat Duis aute irure dolor in reprehenderit in voluptate velit esse cillum dolore eu fugiat nulla pariatur. Excepteur, sint occaecat cupidatat non proident, sunt in culpa qui officia deserunt mollit anim id es laborum.</p>
  <div class="abs video" role="img" aria-label="Video still of a woman in a sun hat in a golden grass field"></div>
  <svg class="abs" style="left:845px;top:204px" width="146" height="146" viewBox="0 0 146 146">
    <circle cx="73" cy="73" r="68" fill="none" stroke="#fff" stroke-width="5"/>
    <path d="M58 45 L104 73 L58 101 Z" fill="none" stroke="#fff" stroke-width="5" stroke-linejoin="round"/>
  </svg>
</section>

<section class="gallery">
  <h2 class="abs section-title" style="left:0;width:1194px;text-align:center;top:30px">GALLERY ACTIVITIES</h2>
  <svg class="abs" style="left:34px;top:212px" width="52" height="40" viewBox="0 0 52 40"><path d="M50 20H4M20 4L4 20l16 16" fill="none" stroke="#111" stroke-width="4"/></svg>
  <svg class="abs" style="left:1112px;top:206px" width="52" height="40" viewBox="0 0 52 40"><path d="M2 20h46M32 4l16 16-16 16" fill="none" stroke="#111" stroke-width="4"/></svg>
  <div class="abs gallery-photo" style="left:115px;width:293px;background:linear-gradient(180deg,#a7b9c4 0%,#c7cfd1 45%,#b5a792 70%,#8d7c66 100%)" role="img" aria-label="Woman doing a camel yoga pose on a beach"></div>
  <div class="abs gallery-photo" style="left:436px;width:300px;background:linear-gradient(180deg,#e6e2dc 0%,#d8d2ca 55%,#c9c2b8 100%)" role="img" aria-label="Woman meditating on a bed in a bright room"></div>
  <div class="abs gallery-photo" style="left:763px;width:322px;background:linear-gradient(150deg,#c9772e 0%,#d99a3f 40%,#8a7a3a 75%,#5f6a2e 100%)" role="img" aria-label="Woman in pink jacket practising alternate nostril breathing in an autumn forest"></div>
</section>

<section class="testimonials">
  <h2 class="abs" style="left:0;width:1234px;top:34px;font-size:40px;font-weight:700">OUR TESTIMONIALS</h2>
  <div class="abs divider" style="left:552px;top:112px"></div>
  <svg class="abs" style="left:34px;top:358px" width="52" height="40" viewBox="0 0 52 40"><path d="M50 20H4M20 4L4 20l16 16" fill="none" stroke="#fff" stroke-width="4"/></svg>
  <svg class="abs" style="left:1118px;top:352px" width="52" height="40" viewBox="0 0 52 40"><path d="M2 20h46M32 4l16 16-16 16" fill="none" stroke="#fff" stroke-width="4"/></svg>

  <div class="abs avatar" style="left:275px;top:144px" role="img" aria-label="Portrait of Lena M."></div>
  <div class="abs testimonial" style="left:100px;top:256px">
    <h4>LENA M.</h4>
    <p>Lorem ipsum dolor sit amet, consectetur adipiscing elit, sed do eiusmod tempor incididunt ut labore et dolore magna aliqua. Ut enim ad minim veniam, quis nostrud exercitation ullamco laboris nisi ut aliquip ex ea commodo consequat Duis aute irure dolor in reprehenderit in voluptate velit esse cillum dolore eu fugiat nulla pariatur. Excepteur, sint occaecat cupidatat non proident, sunt in culpa qui officia deserunt mollit anim id es laborum.</p>
    <div class="stars">
      <svg width="240" height="42" viewBox="0 0 240 42"><g fill="#fff"><path id="star" d="M21 1l6 13 14 2-10 10 2 14-12-7-12 7 2-14L1 16l14-2z"/><use href="#star" x="50"/><use href="#star" x="100"/><use href="#star" x="150"/><use href="#star" x="200"/></g></svg>
    </div>
  </div>

  <div class="abs avatar" style="left:832px;top:140px" role="img" aria-label="Portrait of Mateo"></div>
  <div class="abs testimonial" style="left:648px;top:252px">
    <h4>MATEO</h4>
    <p>Lorem ipsum dolor sit amet, consectetur adipiscing elit, sed do eiusmod tempor incididunt ut labore et dolore magna aliqua. Ut enim ad minim veniam, quis nostrud exercitation ullamco laboris nisi ut aliquip ex ea commodo consequat Duis aute irure dolor in reprehenderit in voluptate velit esse cillum dolore eu fugiat nulla pariatur. Excepteur, sint occaecat cupidatat non proident, sunt in culpa qui officia deserunt mollit anim id es laborum.</p>
    <div class="stars">
      <svg width="240" height="42" viewBox="0 0 240 42"><g fill="#fff"><use href="#star"/><use href="#star" x="50"/><use href="#star" x="100"/><use href="#star" x="150"/><use href="#star" x="200"/></g></svg>
    </div>
  </div>
</section>

<section class="blogs">
  <h2 class="abs teal-title" style="left:0;width:1224px;text-align:center;top:36px">OUR BLOGS</h2>
  <article class="abs blog" style="left:70px;top:126px">
    <div class="blog-photo" style="background:linear-gradient(120deg,#e0742a 0%,#e9b23c 35%,#c9b7a6 60%,#3f6a4a 100%)" role="img" aria-label="Woman shopping for fresh fruit at a market"></div>
    <p>Simple seasonal recipes to nourish your body after a retreat, with fresh market produce, easy weekday ideas and a few of our kitchen team's favourite dishes to share at home.</p>
    <span class="read-more">Read more</span>
  </article>
  <article class="abs blog" style="left:443px;top:124px">
    <div class="blog-photo" style="background:linear-gradient(180deg,#e9e7e8 0%,#d9d5d7 60%,#b7a3b0 100%)" role="img" aria-label="Woman in a side plank yoga pose on a mat"></div>
    <p>A short movement routine you can practise anywhere, combining gentle stretches, balance and strength to wake up the body in the morning or release tension after a long day at work.</p>
    <span class="read-more">Read more</span>
  </article>
  <article class="abs blog" style="left:823px;top:124px">
    <div class="blog-photo" style="background:linear-gradient(160deg,#8c5a66 0%,#b8848b 40%,#6d4a3c 70%,#a36a5c 100%)" role="img" aria-label="Friends stacking their hands together"></div>
    <p>Why shared moments matter: stories from our guests about the friendships born during a stay, and simple ways to keep that sense of connection alive once you return to daily life.</p>
    <span class="read-more">Read more</span>
  </article>
</section>

<section class="contact">
  <div class="contact-photo" role="img" aria-label="Soft-focus outdoor scene with a woman with curly red hair"></div>
  <div class="abs thanks-photo" role="img" aria-label="Smiling woman in a red top"></div>
  <div class="abs thanks-panel">
    <h2>THANK YOU !</h2>
    <p>One of our agen will contact you shortly to give you more information</p>
    <div class="btn-download">DOWNLOAD<br>INFORMATION PACKAGE</div>
  </div>
  <div class="abs newsletter-title">SIGN UP FOR NEWSLETTER</div>
  <div class="abs email">YOUR EMAIL ADDRESS</div>
  <div class="abs btn-signup">SIGN UP</div>
</section>

<footer class="footer">
  <div class="abs footer-brand">FOLLOW THE TIDE</div>
  <nav class="footer-nav">
    <a style="left:456px;top:62px">HOME</a>
    <a style="left:568px;top:62px">OUR STORY</a>
    <a style="left:740px;top:62px">SERVICES</a>
    <a style="left:527px;top:100px">THE TEAM</a>
    <a style="left:675px;top:100px">CONTACT</a>
  </nav>
  <svg class="abs footer-icon" style="left:946px" viewBox="0 0 46 46" aria-label="Email">
    <rect x="4" y="10" width="38" height="28" rx="3" fill="none" stroke="#fff" stroke-width="3"/>
    <path d="M5 12l18 14 18-14" fill="none" stroke="#fff" stroke-width="3"/>
  </svg>
  <svg class="abs footer-icon" style="left:1003px" viewBox="0 0 46 46" aria-label="Video channel">
    <circle cx="23" cy="23" r="20" fill="#e02020"/>
  </svg>
  <svg class="abs footer-icon" style="left:1058px" viewBox="0 0 46 46" aria-label="Location">
    <path d="M23 4c-8 0-14 6-14 14 0 10 14 24 14 24s14-14 14-24c0-8-6-14-14-14z" fill="none" stroke="#fff" stroke-width="3"/>
    <circle cx="23" cy="18" r="5" fill="#fff"/>
  </svg>
  <svg class="abs footer-icon" style="left:1114px" viewBox="0 0 46 46" aria-label="Phone">
    <circle cx="23" cy="23" r="20" fill="none" stroke="#fff" stroke-width="3"/>
    <path d="M15 13c2-2 4-1 5 1l2 4c1 2 0 3-1 4 1 3 3 5 6 6 1-1 2-2 4-1l4 2c2 1 3 3 1 5-3 3-9 2-15-4s-9-13-6-17z" fill="#fff"/>
  </svg>
  <div class="abs copyright">Copyright&nbsp; 2025 Follow The Tide. All rights reserved.</div>
</footer>

</body>
</html>
```